Black Granite Web Design Project

We are looking for a design for a new company that will be selling Black Granite slabs and tiles. We will be selling to both end-consumers and granite installers. We have already settled on a logo and hopefully this will give an idea of what we like in our designs. We are not going to be selling online but want people to call us so the site is basically an enhanced business card. We will be focusing a lot on SEO so the design will have to keep that in mind.

We would like to keep the design in 1024x768 to make it easily view-able on all devices.

Regarding navigation there should only be a few sub-pages, like "Granite Slabs", "Granite Tiles", "Delivery", "Contact"

Aside from that we are open to designs. One idea we did have was to personalize the site and have a person there somehow to represent the company, making the user feel there are real people behind this site. This is just an idea and not a must.

The name of the company and site is "Silver Brook Petrano"

Thanks
Updates

Hello All,

Thanks for the great designs. There are some good looking designs that show beautiful kitchens but this site is made for the granite installers and not the retail consumers. So in order not to to confuse the buyers I would like to keep this as much about the raw products as possible. The raw products being the granite slabs, thereby making it obvious we don't sell granite counter tops. 

This design will really be the identity of this company so it is important we get the right message across on this index page and that this page is as complete as possible.

Again, thanks for all the work being put into this.

Target Market(s)

The target audience is granite installers or companies that would with granite slabs.

Industry/Entity Type

Business

```html
<!DOCTYPE html>
<html lang="en">
<head>
<meta charset="utf-8">
<title>Silver Brook Petrano – Black Granite Slabs and Tiles</title>
<link rel="stylesheet" href="https://fonts.googleapis.com/css2?family=Ropa+Sans&family=Arimo:wght@400&display=swap">
<style>
:root{
  --ink:#1b1b1b;
  --green:#2f5a2a;
  --green-light:#4b7d3c;
  --charcoal:#3b3a3f;
  --card-bg:#efefef;
  --hero-bg:#e6e6e6;
  --line:#cfcfcf;
  --field-border:#c4c4c4;
  --muted:#a5a5a5;
  --white:#ffffff;
  --stone:#121212;
}
*{box-sizing:border-box;margin:0;padding:0}
html,body{width:1043px;height:1200px;overflow:hidden;background:var(--white)}
body{position:relative;font-family:"Arimo",Arial,sans-serif;color:var(--ink)}
.display{font-family:"Ropa Sans",sans-serif}

.site-header{position:absolute;left:0;top:0;width:1043px;height:134px;
  background:linear-gradient(#c9c9c9 0%,#efefef 45%,#fafafa 100%);border-bottom:1px solid #333}
.brand{position:absolute;left:53px;top:60px;display:flex;align-items:center;gap:8px}
.brand-mark{width:18px;height:18px;background:var(--green)}
.brand-name{font-family:"Ropa Sans",sans-serif;font-size:19px;color:var(--ink)}
.header-phone{position:absolute;right:99px;top:30px;display:flex;align-items:center;gap:8px;
  font-family:"Ropa Sans",sans-serif;font-size:25px;color:var(--ink)}
.main-nav{position:absolute;right:42px;top:97px;display:flex;gap:31px;
  font-family:"Ropa Sans",sans-serif;font-size:17px;letter-spacing:.6px}
.main-nav a{color:var(--ink);text-decoration:none}
.main-nav a.is-active{color:var(--green)}

.hero{position:absolute;left:0;top:135px;width:1043px;height:356px;
  background:radial-gradient(ellipse at 40% 50%,#f4f4f4 0%,var(--hero-bg) 70%,#dcdcdc 100%);
  border-bottom:1px solid #333}
.hero-copy{position:absolute;left:71px;top:85px;font-family:"Ropa Sans",sans-serif;color:#2a2a2a}
.hero-copy .lead{font-size:27px;line-height:36px}
.hero-copy .claim{font-size:30px;line-height:36px}
.btn-more{position:absolute;left:75px;top:200px;width:97px;height:31px;
  background:linear-gradient(var(--green-light),var(--green));border:1px solid #244520;
  color:var(--white);font-family:"Ropa Sans",sans-serif;font-size:20px;
  display:flex;align-items:center;justify-content:center;gap:8px}
.hero-tiles{position:absolute;left:660px;top:18px}
.slider-dots{position:absolute;left:477px;top:337px;width:114px;height:20px;background:var(--green);
  border-radius:10px 10px 0 0;display:flex;justify-content:center;align-items:center;gap:6px}
.slider-dots span{width:9px;height:9px;border-radius:50%;background:var(--white)}
.slider-dots span.is-dim{background:#b9b9b9}

.product-card{position:absolute;top:520px;width:417px;height:311px;background:var(--card-bg);
  box-shadow:0 8px 6px -4px rgba(0,0,0,.55)}
.product-card.slab{left:68px}
.product-card.tile{left:554px}
.product-card h2{height:48px;background:var(--charcoal);color:var(--white);
  font-family:"Ropa Sans",sans-serif;font-weight:400;font-size:25px;line-height:48px;padding-left:15px}
.product-photo{height:157px}
.slab .product-photo{background:linear-gradient(160deg,#9a9a9a 0%,#1c1c22 35%,#121216 65%,#8a8a8a 100%)}
.tile .product-photo{background:linear-gradient(180deg,#1a1a1c 0%,#101012 80%,#9c9c9c 100%)}
.product-card p{font-size:12.5px;line-height:16px;color:#333;padding:21px 15px 0 15px}
.card-more{position:absolute;right:37px;bottom:21px;font-family:"Ropa Sans",sans-serif;font-size:17px;
  color:var(--green);display:flex;align-items:center;gap:6px}

.contact-title{position:absolute;left:55px;top:855px;font-family:"Ropa Sans",sans-serif;font-size:27px;font-weight:400}
.contact-rule{position:absolute;left:55px;top:891px;width:921px;height:3px;background:var(--ink)}
.field{position:absolute;border:1px solid var(--field-border);background:var(--white);
  font-size:13px;color:var(--muted);padding:8px 7px}
.field.name{left:63px;top:925px;width:271px;height:28px;padding-top:7px}
.field.email{left:63px;top:968px;width:271px;height:28px;padding-top:7px}
.field.message{left:349px;top:928px;width:273px;height:67px;padding:6px 18px}
.btn-send{position:absolute;left:545px;top:1007px;width:70px;height:31px;border-top:2px solid #ddd;border-left:2px solid #ddd;
  background:#666;color:var(--white);font-size:16px;display:flex;align-items:center;justify-content:center}
.contact-divider{position:absolute;left:687px;top:915px;width:1px;height:142px;background:var(--line)}
.contact-card{position:absolute;left:724px;top:921px;width:238px;font-size:13px;line-height:17px;color:#222}
.contact-card h3{font-family:"Ropa Sans",sans-serif;font-weight:400;font-size:20px;margin-bottom:6px;margin-left:-1px}
.contact-card address{font-style:normal;text-align:justify;margin-bottom:7px}

.site-footer{position:absolute;left:0;top:1089px;width:1043px;height:111px;background:var(--charcoal)}
.social{position:absolute;left:43px;top:17px;display:flex;gap:11px}
.social span{width:31px;height:31px;background:#dcdcdc;border:2px solid #9c9c9c}
.copyright{position:absolute;left:43px;top:79px;font-size:11px;color:var(--white)}
.footer-brand{position:absolute;right:66px;top:40px;display:flex;align-items:center;gap:7px;
  font-family:"Ropa Sans",sans-serif;font-size:17px;color:var(--white)}
.footer-brand .brand-mark{width:14px;height:14px;background:var(--white)}
.footer-rule{position:absolute;left:999px;top:14px;width:1px;height:88px;background:#55545a}
</style>
</head>
<body>
<header class="site-header">
  <div class="brand"><span class="brand-mark"></span><span class="brand-name">SILVER BROOK PETRANO</span></div>
  <div class="header-phone">
    <svg width="26" height="24" viewBox="0 0 26 24" aria-hidden="true">
      <path d="M2 9c0-5 22-5 22 0v2h-6V8c-3-1-7-1-10 0v3H2z" fill="#1b1b1b"/>
      <path d="M6 12h14l3 10H3z" fill="#1b1b1b"/>
      <circle cx="13" cy="17" r="3" fill="#fafafa"/>
    </svg>
    555 210 4478
  </div>
  <nav class="main-nav">
    <a class="is-active" href="#">HOME</a>
    <a href="#">GRANITE SLABS</a>
    <a href="#">GRANITE TILES</a>
    <a href="#">DELIVERY</a>
    <a href="#">CONTACT</a>
  </nav>
</header>

<section class="hero">
  <div class="hero-copy">
    <div class="lead">We are suppliers of</div>
    <div class="claim">BLACK GRANITE SLAB</div>
    <div class="claim">AND BLACK GRANITE TILES</div>
  </div>
  <div class="btn-more">More
    <svg width="8" height="12" viewBox="0 0 8 12" aria-hidden="true"><path d="M0 0l8 6-8 6z" fill="#fff"/></svg>
  </div>
  <svg class="hero-tiles" width="310" height="300" viewBox="0 0 310 300" role="img" aria-label="Three polished black granite tiles arranged in a diamond">
    <ellipse cx="165" cy="292" rx="40" ry="5" fill="rgba(0,0,0,.18)"/>
    <g stroke="#f2f2f2" stroke-width="2" fill="var(--stone)">
      <path d="M165 118l85 85-85 85-85-85z"/>
      <path d="M100 0l85 85-85 85-85-85z"/>
      <path d="M220 0l85 85-85 85-85-85z"/>
    </g>
  </svg>
  <div class="slider-dots"><span></span><span></span><span></span><span class="is-dim"></span></div>
</section>

<article class="product-card slab">
  <h2>GRANITE SLAB</h2>
  <div class="product-photo" role="img" aria-label="Stack of polished black granite slabs"></div>
  <p>Lorem ipsum dolor sit amet cons ectetuer adipiscing elit praesent vestibulu moles lacus aenean nonummy.</p>
  <div class="card-more">MORE
    <svg width="16" height="10" viewBox="0 0 16 10" aria-hidden="true"><path d="M0 5h13M9 1l4 4-4 4" stroke="#2f5a2a" stroke-width="2" fill="none"/></svg>
  </div>
</article>

<article class="product-card tile">
  <h2>GRANITE TILE</h2>
  <div class="product-photo" role="img" aria-label="Black granite tiles laid side by side"></div>
  <p>Lorem ipsum dolor sit amet cons ectetuer adipiscing elit praesent vestibulu moles lacus aenean nonummy.</p>
  <div class="card-more">MORE
    <svg width="16" height="10" viewBox="0 0 16 10" aria-hidden="true"><path d="M0 5h13M9 1l4 4-4 4" stroke="#2f5a2a" stroke-width="2" fill="none"/></svg>
  </div>
</article>

<h2 class="contact-title">Get in touch</h2>
<div class="contact-rule"></div>
<div class="field name">Name</div>
<div class="field email">Email</div>
<div class="field message">Message</div>
<div class="btn-send">Send</div>
<div class="contact-divider"></div>
<div class="contact-card">
  <h3>Silver Brook Petrano</h3>
  <address>Ed. Casa Clara, Ap 45, Rua Serena 12, Leblon, Rio de Janeiro, RJ, CEP-22000-410</address>
  <div>Phone: 555 210 4478</div>
  <div>Email: sales@petrano.com</div>
</div>

<footer class="site-footer">
  <div class="social"><span></span><span></span></div>
  <div class="copyright">Copyright 2013 Silver Brook Petrano. All right reserved.</div>
  <div class="footer-brand"><span class="brand-mark"></span>SILVER BROOK PETRANO</div>
  <div class="footer-rule"></div>
</footer>
</body>
</html>
```